Medical Device - Case Study Template

We need a TEMPLATE that we can reuse to write various case studies about the medical equipment solutions we provide. It will be a double sided letter sized with a modern design that conveys a feeling of expertise, innovation and highly personable service AND be consistent with the brand guide. The content will be divided into a few sections:

- Situation (200-250 words)
- Challenge (100-120 words)
- Solution (100-120 words)
- Results (100-120 words)
- Conclusion (100-120 words)

Additionally, there will need to be a call to action, inviting people to send an email for more information and a short "About Talvo" section (approx. 40 words).

For device picture placeholders, feel free to use any random small benchtop medical device.

```html
<!DOCTYPE html>
<html lang="en">
<head>
<meta charset="utf-8">
<title>Talvo – Medical Equipment Solutions Case Study</title>
<link rel="stylesheet" href="https://fonts.googleapis.com/css2?family=Montserrat:wght@400;500;600&family=Oswald:wght@300;400;500&display=swap">
<style>
  :root {
    --backdrop: #71849a;
    --paper: #ffffff;
    --band: #eeeef0;
    --orange: #ee8c45;
    --ink: #2b2b2b;
    --frame: #8fa6c2;
    --photo-light: #f3f3f5;
    --photo-dark: #dcdde0;
  }
  * { box-sizing: border-box; margin: 0; padding: 0; }
  html, body { width: 1200px; height: 870px; overflow: hidden; }
  body { background: var(--backdrop); position: relative; font-family: "Montserrat", sans-serif; color: var(--ink); }

  .page { position: absolute; background: var(--paper); overflow: hidden; }
  .page--front { left: 70px; top: 68px; width: 519px; height: 733px; }
  .page--back  { left: 614px; top: 70px; width: 516px; height: 730px; }

  /* Front page */
  .front-band { position: absolute; left: 0; right: 0; top: 602px; bottom: 0; background: var(--band); }
  .brand { position: absolute; left: 52px; top: 48px; display: flex; align-items: center; gap: 8px; }
  .brand__mark { width: 26px; height: 26px; background: var(--orange); }
  .brand__name { font-family: "Montserrat", sans-serif; font-weight: 500; font-size: 26px; color: var(--frame); letter-spacing: 1px; line-height: 1; }
  .category { position: absolute; right: 51px; top: 55px; font-family: "Oswald", sans-serif; font-weight: 400; font-size: 13px; color: var(--orange); letter-spacing: -0.2px; }
  .category__bar { position: absolute; right: 51px; top: 76px; width: 45px; height: 8px; background: var(--orange); }
  .hero-photo { position: absolute; left: 51px; top: 127px; width: 416px; height: 277px;
    background: radial-gradient(ellipse at 40% 40%, var(--photo-light), var(--photo-dark)); }
  .headline { position: absolute; left: 60px; top: 362px; font-family: "Oswald", sans-serif; font-weight: 500;
    font-size: 49px; line-height: 62px; color: var(--orange); letter-spacing: -0.5px; text-transform: uppercase; }
  .about { position: absolute; left: 287px; top: 451px; width: 180px; font-size: 8.2px; line-height: 14px; }
  .about strong { font-weight: 600; }
  .contact { position: absolute; left: 52px; top: 556px; width: 186px; height: 126px; border: 1px solid var(--frame); padding: 6px; }
  .contact__panel { width: 100%; height: 100%; background: var(--orange); color: #fff; text-align: center; padding-top: 30px; }
  .contact__line { font-size: 10px; line-height: 14px; }
  .contact__web { margin-top: 13px; font-family: "Oswald", sans-serif; font-weight: 500; font-size: 15px; letter-spacing: 4px; }
  .signoff__bar { position: absolute; left: 290px; top: 618px; width: 12px; height: 64px; background: var(--orange); }
  .signoff { position: absolute; left: 319px; top: 610px; font-family: "Oswald", sans-serif; font-weight: 300; font-size: 19px; line-height: 26px; color: var(--orange); text-transform: uppercase; }

  /* Back page */
  .back-band { position: absolute; left: 0; right: 0; top: 197px; height: 388px; background: var(--band); }
  .section-bar { position: absolute; left: 37px; top: 37px; width: 46px; height: 8px; background: var(--orange); }
  .section-title { position: absolute; left: 37px; top: 53px; font-family: "Oswald", sans-serif; font-weight: 500; font-size: 19px; letter-spacing: 5px; color: var(--orange); }
  .situation { position: absolute; top: 92px; width: 222px; font-size: 7.9px; line-height: 9.4px; }
  .situation p + p { margin-top: 9px; }
  .situation--left { left: 37px; width: 176px; }
  .situation--right { left: 253px; }

  .card { position: absolute; width: 202px; height: 208px; background: var(--paper); border: 1px solid var(--orange); display: flex; }
  .card__label { width: 32px; background: var(--orange); display: flex; align-items: center; justify-content: center; }
  .card__label span { writing-mode: vertical-rl; transform: rotate(180deg); font-family: "Oswald", sans-serif; font-weight: 500; font-size: 17px; color: #fff; text-transform: uppercase; letter-spacing: -0.3px; }
  .card__body { flex: 1; padding: 7px 8px 0 10px; font-size: 7.9px; line-height: 9.4px; }
  .card--challenge { left: 37px; top: 223px; }
  .card--solution { left: 278px; top: 223px; }
  .card--results { left: 37px; top: 461px; }
  .card--conclusion { left: 278px; top: 461px; }
</style>
</head>
<body>

<section class="page page--front">
  <div class="front-band"></div>
  <div class="brand"><span class="brand__mark"></span><span class="brand__name">talvo</span></div>
  <div class="category">MEDICAL TECHNOLOGY</div>
  <div class="category__bar"></div>
  <div class="hero-photo" role="img" aria-label="Photo of a white stethoscope lying on a light grey surface"></div>
  <h1 class="headline">Medical<br>Equipment<br>Solutions</h1>
  <p class="about"><strong>About us:</strong> is simply dummy text of the printing and typesetting industry. Lorem Ipsum has been the industry's standard dummy text ever since the 1500s, when an unknown printer took a galley of type and scrambled it to make a type specimen book.</p>
  <div class="contact">
    <div class="contact__panel">
      <p class="contact__line">5120 Harlow Avenue</p>
      <p class="contact__line">(456) 7310 2294</p>
      <p class="contact__web">TALVO.ORG</p>
    </div>
  </div>
  <div class="signoff__bar"></div>
  <p class="signoff">Talvo<br>Medical<br>Technology</p>
</section>

<section class="page page--back">
  <div class="back-band"></div>
  <div class="section-bar"></div>
  <h2 class="section-title">SITUATION</h2>
  <div class="situation situation--left">
    <p>is simply dummy text of the printing and typesetting industry. Lorem Ipsum has been the industry's standard dummy text ever is simply dummy text of the printing and typesetting industry. Lorem Ipsum has been the industry's standard dummy text ever is simply dummy text of the printing and typesetting industry. Lorem Ipsum has been the industry's standard dummy text ever</p>
  </div>
  <div class="situation situation--right">
    <p>is simply dummy text of the printing and typesetting industry. Lorem Ipsum has been the industry's standard dummy text ever since the 1500s, when an unknown printer took a galley of type and scrambled it to make a type specimen book.</p>
    <p>simply dummy text of the printing and typesetting industry. Lorem Ipsum has been the industry's standard dummy text ever</p>
  </div>

  <article class="card card--challenge">
    <div class="card__label"><span>Challenge</span></div>
    <p class="card__body">Lorem Ipsum is simply dummy text of the printing and typesetting industry. Lorem Ipsum has been the industry's standard dummy text ever since the 1500s, when an unknown printer took a galley of type and scrambled it to make a type specimen book. Lorem Ipsum is simply dummy text of the printing and typesetting industry. Lorem Ipsum has been the industry's standard dummy text ever since the 1500s, when an unknown printer took a galley of type and scrambled it to make a type specimen book. Lorem Ipsum is simply dummy text of the printing and typesetting industry. Lorem Ipsum has been the industry's standard dummy text ever since the 1500s</p>
  </article>
  <article class="card card--solution">
    <div class="card__label"><span>Solution</span></div>
    <p class="card__body">Lorem Ipsum is simply dummy text of the printing and typesetting industry. Lorem Ipsum has been the industry's standard dummy text ever since the 1500s, when an unknown printer took a galley of type and scrambled it to make a type specimen book. Lorem Ipsum is simply dummy text of the printing and typesetting industry. Lorem Ipsum has been the industry's standard dummy text ever since the 1500s, when an unknown printer took a galley of type and scrambled it to make a type specimen book. Lorem Ipsum is simply dummy text of the printing and typesetting industry. Lorem Ipsum has been the industry's standard dummy text ever since the 1500s</p>
  </article>
  <article class="card card--results">
    <div class="card__label"><span>Results</span></div>
    <p class="card__body">Lorem Ipsum is simply dummy text of the printing and typesetting industry. Lorem Ipsum has been the industry's standard dummy text ever since the 1500s, when an unknown printer took a galley of type and scrambled it to make a type specimen book. Lorem Ipsum is simply dummy text of the printing and typesetting industry. Lorem Ipsum has been the industry's standard dummy text ever since the 1500s, when an unknown printer took a galley of type and scrambled it to make a type specimen book. Lorem Ipsum is simply dummy text of the printing and typesetting industry. Lorem Ipsum has been the industry's standard dummy text ever since the 1500s</p>
  </article>
  <article class="card card--conclusion">
    <div class="card__label"><span>Conclusion</span></div>
    <p class="card__body">Lorem Ipsum is simply dummy text of the printing and typesetting industry. Lorem Ipsum has been the industry's standard dummy text ever since the 1500s, when an unknown printer took a galley of type and scrambled it to make a type specimen book. Lorem Ipsum is simply dummy text of the printing and typesetting industry. Lorem Ipsum has been the industry's standard dummy text ever since the 1500s, when an unknown printer took a galley of type and scrambled it to make a type specimen book. Lorem Ipsum is simply dummy text of the printing and typesetting industry. Lorem Ipsum has been the industry's standard dummy text ever since the 1500s</p>
  </article>
</section>

</body>
</html>
```